Lotus Vale is a new opened business in takapuna, Auckland, which provide traditional Chinese Therapeutic & relaxation massage. We like to invite more and more people as our customers, especially for the office people near by in the same suburb. We want this flyer to have a pormotion for these kind of people,the probably content of this pormotion is during their lunch break, they will receive a professional Quckily De-stress Relaxation massage for $20 only. We are not the native speaker so we wouldn't use specific sentence to describe. We like the ad be academic and professional.The color we want to use is the same as the file we have attached.also in the flyer we need the direction for the location of our shop.
Massage
Must have
- have a pormotion for office people,the probably content of this pormotion is during their lunch break, they will receive a professional Quckily De-stress Relaxation massage for $20 only.
Nice to have
- our shop address is shop 7, 41 - 55 Brindlecombe Road, Takapuna, Auckland.
Phone number: 09-5317208
Email: lotusvale.nz@examplemail.com
we need the direction for the location of our shop (map)

```html
<!DOCTYPE html>
<html lang="en">
<head>
<meta charset="utf-8">
<title>Lotus Vale – Lunch Break Massage Flyer</title>
<link rel="stylesheet" href="https://fonts.googleapis.com/css2?family=Lobster&family=Mulish:ital,wght@0,400;0,800;1,800&display=swap">
<style>
  :root{
    --page:#ffffff;
    --brown:#553312;
    --brown-line:#6b4420;
    --orange:#f0782b;
    --cream:#fff8e8;
    --butter:#fbe1a6;
    --amber:#f8c760;
    --dot:#f6ac52;
    --photo-a:#d9a98a;
    --photo-b:#f2d7c4;
    --photo-c:#b98a6c;
  }
  *{box-sizing:border-box;margin:0;padding:0}
  html,body{width:1200px;height:763px;overflow:hidden;background:var(--page)}
  body{position:relative;font-family:"Mulish",sans-serif;color:var(--brown)}

  .flyer{
    position:absolute;top:81px;width:412px;height:586px;overflow:hidden;
    background:linear-gradient(160deg,var(--cream) 0%,var(--butter) 55%,var(--amber) 100%);
    box-shadow:0 4px 14px rgba(0,0,0,.18);
  }
  .flyer--wide{left:127px}
  .flyer--compact{left:667px}

  .flyer__photo{
    position:absolute;left:0;top:0;width:412px;height:215px;
    background:linear-gradient(120deg,var(--photo-c) 0%,var(--photo-a) 35%,var(--photo-b) 70%,#f6f1ec 100%);
  }
  .flyer__shapes{position:absolute;left:0;top:0;width:412px;height:586px}

  .brand{
    position:absolute;left:200px;top:216px;width:190px;height:26px;
    display:flex;align-items:center;justify-content:center;gap:8px;
    font-family:"Mulish",sans-serif;font-weight:800;font-size:20px;line-height:1;color:var(--brown);
  }
  .brand__dot{width:18px;height:18px;border-radius:50%;background:var(--orange);flex:none}

  .headline{position:absolute;left:20px;font-weight:400;white-space:nowrap;letter-spacing:-.3px}
  .headline b{font-weight:800}
  .headline .name{font-family:"Lobster",cursive;font-weight:400;letter-spacing:.2px}

  .offer{position:absolute;left:20px;color:var(--orange);white-space:nowrap}
  .offer b{font-weight:800}
  .offer .price{font-weight:800}

  .services{position:absolute;left:20px;font-weight:800;white-space:nowrap}
  .services__title{font-style:italic}
  .services ul{list-style:none}
  .services li::before{content:"• "}

  /* wide variant */
  .flyer--wide .headline{top:248px;font-size:31px;line-height:39px}
  .flyer--wide .headline .name{font-size:34px}
  .flyer--wide .offer{top:368px;font-size:22px;line-height:31px}
  .flyer--wide .offer .price{font-size:31px}
  .flyer--wide .services{top:504px;font-size:14px;line-height:17px}

  /* compact variant */
  .flyer--compact .headline{top:250px;font-size:26px;line-height:38px}
  .flyer--compact .headline .name{font-size:30px}
  .flyer--compact .offer{top:331px;font-size:22px;line-height:31px}
  .flyer--compact .offer .price{font-size:30px}
  .flyer--compact .services{top:474px;font-size:16px;line-height:23px}
</style>
</head>
<body>

<article class="flyer flyer--wide">
  <div class="flyer__photo" role="img" aria-label="Photo of a woman relaxing face down while receiving a back and shoulder massage"></div>
  <svg class="flyer__shapes" viewBox="0 0 412 586" aria-hidden="true">
    <path d="M0 140 Q190 225 412 180 L412 586 L0 586 Z" fill="var(--cream)"/>
    <path d="M0 140 Q190 225 412 180 L412 195 Q190 235 0 170 Z" fill="#ffffff"/>
    <path d="M0 170 Q190 235 412 195" fill="none" stroke="var(--brown-line)" stroke-width="3"/>
    <circle cx="420" cy="400" r="75" fill="var(--dot)"/>
    <circle cx="410" cy="580" r="62" fill="var(--dot)"/>
  </svg>
  <div class="brand"><span class="brand__dot"></span>Lotus Vale</div>
  <h1 class="headline"><span class="name">Lotus Vale</span> the <b>NEW</b><br>method to <b>RELAX</b> on<br>your <b>LUNCH BREAK!</b></h1>
  <p class="offer">Get a professional<br><b>Quckily De-stress</b><br><b>Relaxation massage</b><br>for <span class="price">$20</span><b>only</b></p>
  <div class="services">
    <p class="services__title">We specialize in:</p>
    <ul><li>Sports massage</li><li>Therapeutic/remedial massage</li><li>Relaxation massage</li></ul>
  </div>
</article>

<article class="flyer flyer--compact">
  <div class="flyer__photo" role="img" aria-label="Photo of a woman relaxing face down while receiving a back and shoulder massage"></div>
  <svg class="flyer__shapes" viewBox="0 0 412 586" aria-hidden="true">
    <path d="M0 140 Q190 225 412 180 L412 586 L0 586 Z" fill="var(--cream)"/>
    <path d="M0 140 Q190 225 412 180 L412 195 Q190 235 0 170 Z" fill="#ffffff"/>
    <path d="M0 170 Q190 235 412 195" fill="none" stroke="var(--brown-line)" stroke-width="3"/>
    <circle cx="420" cy="400" r="75" fill="var(--dot)"/>
    <circle cx="410" cy="580" r="62" fill="var(--dot)"/>
  </svg>
  <div class="brand"><span class="brand__dot"></span>Lotus Vale</div>
  <h1 class="headline"><span class="name">Lotus Vale</span> the <b>NEW</b><br>method for <b>LUNCH BREAK!</b></h1>
  <p class="offer">Get a professional<br><b>Quckily De-stress</b><br><b>Relaxation massage</b><br>for <span class="price">$20</span><b>only</b></p>
  <div class="services">
    <p class="services__title">We specialize in:</p>
    <ul><li>Sports massage</li><li>Therapeutic/remedial massage</li><li>Relaxation massage</li></ul>
  </div>
</article>

</body>
</html>
```